Hollow Fern Kentucky Bourbon Whiskey

We need a label design for a bottle of whiskey. It is for a 750 ml bottle and needs to have a place to write in proof, age, and bottle number at bottom of label. It is a single barrel bourbon. We want to include our tree logo attached in the upload files in some way. Leave out the Distillery part to where it just says Hollow Fern Bourbon Whiskey with the tree. We need the label to be clean and modern. I have also attached a picture of the bottle the label is intended to go on.

Industry/Entity Type

Bourbon

Requirements
Must have
• Hollow Fern tree from file

```html
<!DOCTYPE html>
<html lang="en">
<head>
<meta charset="utf-8">
<title>Hollow Fern Kentucky Bourbon Whiskey — Label</title>
<link href="https://fonts.googleapis.com/css2?family=Cinzel:wght@400;500&family=Libre+Caslon+Display&family=Pinyon+Script&family=Caveat:wght@400&family=Libre+Caslon+Text:wght@400&display=swap" rel="stylesheet">
<style>
  :root {
    --page: #ffffff;
    --label: #262626;
    --label-deep: #1d1d1d;
    --gold: #e3bd45;
    --gold-deep: #b4892a;
    --cream: #f2f0ea;
    --panel: #e3e3e0;
    --panel-ink: #4c4c4c;
    --pen: #5a7bb7;
  }
  * { margin: 0; padding: 0; box-sizing: border-box; }
  html, body { width: 1200px; height: 1200px; overflow: hidden; background: var(--page); }
  .canvas { position: relative; width: 1200px; height: 1200px; }

  .label {
    position: absolute; left: 268px; top: 50px;
    width: 663px; height: 1101px;
    background: radial-gradient(ellipse at 50% 35%, #2c2c2c 0%, var(--label) 55%, var(--label-deep) 100%);
    color: var(--cream);
    text-align: center;
  }

  .brand-mark {
    position: absolute; left: 50%; top: 92px;
    width: 150px; height: 150px; margin-left: -75px;
    border-radius: 50%;
    background: linear-gradient(160deg, var(--gold) 0%, var(--gold-deep) 100%);
  }
  .brand-rule {
    position: absolute; top: 285px; height: 3px; width: 160px;
    background: linear-gradient(90deg, var(--gold-deep), var(--gold));
  }
  .brand-rule.left { left: 105px; }
  .brand-rule.right { right: 105px; }
  .brand-name {
    position: absolute; left: 0; right: 0; top: 300px;
    font-family: "Cinzel", serif; font-weight: 500;
    font-size: 58px; letter-spacing: 1px; color: var(--cream);
  }
  .brand-underline {
    position: absolute; top: 393px; height: 3px; width: 110px;
    background: var(--gold);
  }
  .brand-underline.left { left: 75px; }
  .brand-underline.right { right: 75px; }

  .style-name {
    position: absolute; left: 0; right: 0; top: 545px;
    font-family: "Libre Caslon Display", serif;
    font-size: 68px; color: var(--cream);
  }
  .style-kind {
    position: absolute; left: 0; right: 0; top: 638px;
    font-family: "Libre Caslon Display", serif;
    font-size: 86px; letter-spacing: 2px;
    color: var(--gold);
  }

  .facts {
    position: absolute; left: 30px; right: 30px; top: 833px;
    display: flex; align-items: center; justify-content: space-between;
  }
  .fact {
    font-family: "Libre Caslon Text", serif;
    font-size: 19px; line-height: 1.05; color: #cfcfcf;
    text-transform: uppercase;
  }
  .fact.volume { text-align: left; }
  .fact.strength { text-align: center; }
  .cask {
    display: flex; align-items: center; gap: 14px;
    font-family: "Pinyon Script", cursive;
    font-size: 40px; color: var(--cream);
  }
  .cask .dot { width: 9px; height: 9px; background: var(--gold); }

  .gold-band {
    position: absolute; left: 0; right: 0; top: 940px; height: 20px;
    background: linear-gradient(90deg, var(--gold-deep), var(--gold) 30%, #f3d878 50%, var(--gold) 70%, var(--gold-deep));
  }
  .record {
    position: absolute; left: 0; right: 0; top: 960px; height: 120px;
    background: var(--panel);
    display: grid; grid-template-columns: 170px 1fr 140px;
    align-items: center;
  }
  .record-cell {
    height: 90px; display: flex; flex-direction: column; align-items: center; justify-content: center;
  }
  .record-cell + .record-cell { border-left: 2px solid #7d7d7d; }
  .record-title {
    font-family: "Libre Caslon Text", serif;
    font-size: 34px; color: var(--panel-ink); text-transform: uppercase;
    letter-spacing: -0.5px;
  }
  .record-entry {
    font-family: "Caveat", cursive;
    font-size: 36px; line-height: 1; color: var(--pen);
  }
  .label-foot {
    position: absolute; left: 0; right: 0; bottom: 0; height: 21px;
    background: var(--label-deep);
  }
</style>
</head>
<body>
<main class="canvas">
  <section class="label" aria-label="Hollow Fern Kentucky Bourbon Whiskey bottle label">
    <div class="brand-mark" aria-hidden="true"></div>
    <div class="brand-rule left"></div>
    <div class="brand-rule right"></div>
    <h1 class="brand-name">HOLLOW FERN</h1>
    <div class="brand-underline left"></div>
    <div class="brand-underline right"></div>

    <p class="style-name">Kentucky Bourbon</p>
    <p class="style-kind">WHISKEY</p>

    <div class="facts">
      <p class="fact volume">750 ML<br>NET.WT</p>
      <p class="cask"><span class="dot"></span>Single Barrel Bourbon<span class="dot"></span></p>
      <p class="fact strength">42%<br>ALC/VOL</p>
    </div>

    <div class="gold-band"></div>
    <div class="record">
      <div class="record-cell">
        <span class="record-title">Proof</span>
        <span class="record-entry">80</span>
      </div>
      <div class="record-cell">
        <span class="record-title">Bottle Number</span>
        <span class="record-entry">12/125</span>
      </div>
      <div class="record-cell">
        <span class="record-title">Age</span>
        <span class="record-entry">3 years</span>
      </div>
    </div>
    <div class="label-foot"></div>
  </section>
</main>
</body>
</html>
```